Media Company Needs Homepage Design

We need a homepage design for our studio. Our media company works with a network of on-camera talent and experts to create quality content for the internet. We are targeting top talent in various industries to join our network to star in online video series, write articles, and share their expertise with the world.

We share knowledge with the world and would like our homepage to communicate that. We'd also like for it to appeal to an accomplished audience looking to build their brand and stand out in their industry. Think 'sleek,' 'modern' and 'visual.'

The main message is: 'Create, Engage, Stand Out' and our tagline is: "The Platform for Influential Voices.'

Our secondary message with a call to action:
We offer an innovative way for you to promote yourself to new audiences through original content.
Call to action: Partner with us

Hi all,

Just a few days left to submit a design. We'd love to see what you come up with! Please message with any questions.

Thank you!

Industry/Entity Type

Internet

Requirements
Must have
• Focus on 'stand out' as primary message in 'create, engage, stand out.' Our target audience is looking for ways to stand out in their industry.
Nice to have
• Could focus on the words 'create, engage, stand out' and play with various type treatments. Words as primary imagery. See attached photo for example.

Could focus on knowledge as primary concept and imagery. example: brainwaves, books, sharing knowledge, knowledge is power.

Could include space for two less prominent sub sections for copy and call-to-action

Could focus on bold, creative imagery. See attached photo for example.

```html
<!DOCTYPE html>
<html lang="en">
<head>
<meta charset="utf-8">
<title>Title — The Platform for Influential Voices</title>
<link rel="stylesheet" href="https://fonts.googleapis.com/css2?family=Noto+Serif&family=Open+Sans:wght@300;400;600&display=swap">
<style>
  :root {
    --header-top: #2f6ea6;
    --hero-top: #2a64a0;
    --hero-bottom: #0c3f8f;
    --band: #0d2d66;
    --ring: #0e2c62;
    --footer: #0a1b3a;
    --rule: #7fb0dc;
    --headline: #d3e3f6;
    --text: #ffffff;
    --link: #dfe9f5;
    --feature-title: #f6ead8;
    --button-top: #f4f8ff;
    --button-bottom: #a9c6ec;
    --button-text: #14213a;
  }
  * { box-sizing: border-box; margin: 0; padding: 0; }
  html, body { width: 1200px; height: 1148px; overflow: hidden; }
  body {
    position: relative;
    font-family: "Open Sans", sans-serif;
    color: var(--text);
    background: var(--footer);
  }
  .page { position: absolute; inset: 0; }

  .hero-bg {
    position: absolute; left: 0; top: 0; width: 1200px; height: 544px;
    background: linear-gradient(180deg, var(--hero-top) 0%, #1d559b 40%, var(--hero-bottom) 100%);
  }
  .feature-bg {
    position: absolute; left: 0; top: 544px; width: 1200px; height: 423px;
    background: var(--band);
  }
  .footer-bg {
    position: absolute; left: 0; top: 967px; width: 1200px; height: 181px;
    background: var(--footer);
    border-top: 1px solid #173264;
  }

  .site-header {
    position: absolute; left: 0; top: 0; width: 1200px; height: 71px;
    background: var(--header-top);
    border-bottom: 1px solid var(--rule);
  }
  .site-title {
    position: absolute; left: 43px; top: 12px;
    font-size: 37px; font-weight: 400; letter-spacing: 1px;
  }
  .site-nav {
    position: absolute; right: 72px; top: 30px;
    font-size: 17px; color: var(--link); letter-spacing: 0.5px;
  }
  .site-nav a { color: var(--link); text-decoration: none; }
  .site-nav .sep { margin: 0 10px; }

  .hero-title {
    position: absolute; left: 43px; top: 112px; width: 520px;
    font-family: "Noto Serif", serif; font-weight: 400;
    font-size: 52px; line-height: 60px; letter-spacing: 2.5px;
    color: var(--headline); word-spacing: 14px;
  }
  .hero-copy {
    position: absolute; left: 51px; top: 245px; width: 523px;
    font-size: 16.5px; line-height: 21px; text-align: justify; letter-spacing: 0.6px;
  }
  .cta {
    position: absolute; left: 49px; top: 350px; width: 322px; height: 66px;
    border: 3px solid #ffffff; border-radius: 7px;
    background: linear-gradient(180deg, var(--button-top), var(--button-bottom));
    color: var(--button-text); font-size: 23px; font-weight: 400; letter-spacing: 0.8px;
    display: flex; align-items: center; padding-left: 32px; gap: 22px;
    text-decoration: none;
  }
  .product-preview {
    position: absolute; left: 684px; top: 105px; width: 445px; height: 300px;
    background: linear-gradient(160deg, #3b3f47 0%, #14171d 55%, #2b5c8c 100%);
    border: 2px solid #c9ccd2; border-radius: 3px;
  }

  .feature-ring {
    position: absolute; width: 286px; height: 286px; border-radius: 50%;
    background: var(--ring);
  }
  .feature-disc {
    position: absolute; width: 254px; height: 254px; border-radius: 50%;
    background: #dfe8f6; border: 4px solid #f4f7fc;
    box-shadow: inset 0 0 0 4px #b9cce8;
    overflow: hidden;
  }
  .feature-art { width: 100%; height: 100%; }
  .art-create { background: radial-gradient(circle at 50% 60%, #ffffff 45%, #f6e3d8 70%, #f0f2f7 100%); }
  .art-engage { background: radial-gradient(circle at 50% 55%, #ffffff 35%, #d8f0e0 60%, #f1f4fa 100%); }
  .art-standout { background: radial-gradient(circle at 45% 45%, #d4232b 0%, #7a1a1f 45%, #2b2b2e 75%, #e8e8e8 100%); }

  .feature-title {
    position: absolute; top: 745px;
    font-size: 44px; font-weight: 300; letter-spacing: 1.5px;
    color: var(--feature-title);
    text-shadow: 0 0 8px rgba(255, 200, 140, 0.55);
  }
  .feature-copy {
    position: absolute; top: 811px; width: 247px;
    font-size: 16.5px; line-height: 20px; text-align: justify; letter-spacing: 0.4px;
  }

  .footer-heading {
    position: absolute; top: 988px;
    font-size: 31px; font-weight: 400; letter-spacing: 0.5px;
  }
  .address {
    position: absolute; left: 93px; top: 1044px; width: 256px;
    font-size: 16.5px; line-height: 20px; text-align: justify; letter-spacing: 0.4px;
    font-style: normal;
  }
  .social {
    position: absolute; left: 492px; top: 1046px;
    display: flex; gap: 22px; font-size: 18px; color: var(--link);
  }
  .social a { color: var(--link); text-decoration: none; display: flex; align-items: center; gap: 7px; }
  .social .dot { width: 10px; height: 10px; border-radius: 50%; background: var(--link); }
  .copyright {
    position: absolute; right: 17px; top: 1118px;
    font-size: 14px; letter-spacing: 0.4px;
  }
</style>
</head>
<body>
<div class="page">
  <div class="hero-bg"></div>
  <div class="feature-bg"></div>
  <div class="footer-bg"></div>

  <header class="site-header">
    <div class="site-title">Title</div>
    <nav class="site-nav">
      <a href="#">link1</a><span class="sep">|</span><a href="#">link 2</a><span class="sep">|</span><a href="#">link3</a><span class="sep">|</span><a href="#">link4</a>
    </nav>
  </header>

  <h1 class="hero-title">The Platform for Influential voices</h1>
  <p class="hero-copy">Porta fusce varius natoque penatibus magnis. Montes nascetr mugiat suada odio. Porta fusce varius natoque penatibus magnis. Montes nascetr mugiat suada odio.</p>
  <a class="cta" href="#">PARTNER WITH US
    <svg width="18" height="18" viewBox="0 0 18 18" aria-hidden="true"><path d="M4 2 L15 9 L4 16 Z" fill="#14213a"/></svg>
  </a>
  <div class="product-preview" role="img" aria-label="Screenshot of the video editing studio with clip thumbnails and a preview player"></div>

  <div class="feature-ring" style="left:30px; top:463px;"></div>
  <div class="feature-ring" style="left:341px; top:463px;"></div>
  <div class="feature-ring" style="left:650px; top:451px;"></div>

  <div class="feature-disc" style="left:46px; top:479px;">
    <div class="feature-art art-create" role="img" aria-label="Illustration of a pencil drawing the word create"></div>
  </div>
  <div class="feature-disc" style="left:357px; top:479px;">
    <div class="feature-art art-engage" role="img" aria-label="Illustration of colourful letter blocks spelling engage"></div>
  </div>
  <div class="feature-disc" style="left:666px; top:467px;">
    <div class="feature-art art-standout" role="img" aria-label="Word cloud sphere with the words stand out"></div>
  </div>

  <h2 class="feature-title" style="left:89px;">CREATE</h2>
  <h2 class="feature-title" style="left:403px;">ENGAGE</h2>
  <h2 class="feature-title" style="left:706px;">STANDOUT</h2>

  <p class="feature-copy" style="left:87px;">Porta fusce varius natoque penatibus magnis. Montes nascetr mugiat suada odio. Porta fusce varius natoque penatibus magnis. Montes nascetr mugiat suada odio.</p>
  <p class="feature-copy" style="left:402px;">Porta fusce varius natoque penatibus magnis. Montes nascetr mugiat suada odio. Porta fusce varius natoque penatibus magnis. Montes nascetr mugiat suada odio.</p>
  <p class="feature-copy" style="left:708px;">Porta fusce varius natoque penatibus magnis. Montes nascetr mugiat suada odio. Porta fusce varius natoque penatibus magnis. Montes nascetr mugiat suada odio.</p>

  <h3 class="footer-heading" style="left:89px;">Contact Us</h3>
  <address class="address">Address ,Address, Address, Address, Address<br>Address ,Address, Address, Address, Address</address>

  <h3 class="footer-heading" style="left:488px;">Follow us</h3>
  <div class="social">
    <a href="#"><span class="dot"></span>Chirpline</a>
    <a href="#"><span class="dot"></span>Friendbook</a>
  </div>

  <p class="copyright">Copyright 2012. all rights reserved</p>
</div>
</body>
</html>
```